Label for a new, ambitious & organic Loire valley still & sparkling white wine

In the uploaded items, I have added a brief which explains what I expect.

Ultimately, I need a complete visual identity which can be used on a website, on stationary, on packaging, clothes etc. First step is the front label of the wine bottles.

The estate is called Clos de XYZ (name to be releaved at a later stage) and is located in Vouvray appellation. It produces still and sparkling white wines based on the Chenin grape. Chenin is a niche grape compared to Sauvignon and Chardonnay. Customers are typically :
a) enlightened wine amateurs who value quality of product more than the price tag
b) chenin geeks – the vast majority of the world’s production is concentrated in south Africa and Loire valley so it is a bit of a monopoly
c) foodies – chenin is great for gastronomical food
d) people seeking natural / organic / biodynamic wines

The winey exists today but sells most of its wine to wholesalers and the quality is average. Its own brand is close to non-existent. I am keeping the name (clos de XYZ) but the wines will be of much higher quality. Market segment will be premium (for chenin wine) which corresponds to a 15-40 € price range.

As I am an outsider to the wine world, and have a much higher ambition than the average producer in that region, the graphical identity could include a “new kid on the block” / “innovation” / “stand out” effect. On the other hand, the Loire valley, the winery and our work methods are anchored in century long traditions. And the product is decidedly French. So the message should be “head in the sky and feet solidly anchored in the soil” or “a modern product anchored in tradition”.
The wine is organic, heading toward biodynamic and we will work hard to reduce, along the entire value chain, our environmental footprint.
We will work according to natural, traditional methods, letting the grapes, the soil and the weather express the stories they have to tell. The wines will not be ‘technical’ wines made with additives and technology.
The most iconic monument of the Vouvray wine area is the church tower which can be seen on the Lexorama page (also uploaded as part of the brief) : https://fr.lexorama-ency.org/article/Vouvray_%28AOC%29
The silhouette of the tower could be a salient graphical element – maybe even a totemic element.

The bottle shapes will be traditional ones because innovating on bottle design comes at a great cost. There is more impact/unit cost in the label. However, we will be exploring innovative bottling options for the sake of reducing the carbon footprint and most likely, there will not be much wiggle room for creative designs.
I like simple, clean (but not clinical), precise, stylish and timeless design.
We will produce still and sparking. For each category there will be 2 to 5 different wines. All wines will have in common : grape sort, Clos de XYZ and Vouvray appellation. Differences will be sparkling or not, dry or a little residual sugar, which parcel of land the grapes come from and how we made the wine. Sparkling or non-sparkling is obvious from the bottle. So the information that needs to be fitted on the front label (there will also be a more technical and regulated back label) is : Clos de XYZ, Vouvray, Chenin and then a difference name for each wine (cuvée in French). The latter could be the names of the plots/parcels of land. For example : Le Brolin

Target Market(s)

included in project description

Industry/Entity Type

wine

Requirements
Must have
• a more or less stylized profile of the Vouvray church tower
Nice to have
• a little V notch at the top of the label which suggests the 2 Vs of Vouvray

```html
<!DOCTYPE html>
<html lang="fr">
<head>
<meta charset="utf-8">
<title>Clos des Aubrelles – Chenin Vouvray</title>
<link rel="stylesheet" href="https://fonts.googleapis.com/css2?family=Cormorant+SC:wght@500&family=Cormorant+Garamond:wght@500&family=Pinyon+Script&display=swap">
<style>
  :root {
    --stage: #c4c4c4;
    --stage-light: #e6e6e6;
    --strip: #ffffff;
    --paper: #f7f1ec;
    --gold: #f0a21e;
    --ink: #2b2b2b;
    --art-dark: #4a4a4a;
    --art-leaf: #e9a92a;
  }
  * { box-sizing: border-box; margin: 0; padding: 0; }
  html, body { width: 1200px; height: 1111px; overflow: hidden; }
  body {
    position: relative;
    background: radial-gradient(ellipse at 58% 55%, var(--stage-light) 0%, var(--stage) 60%);
    font-family: "Cormorant Garamond", serif;
    color: var(--ink);
  }
  .brand-strip {
    position: absolute; left: 0; top: 0;
    width: 244px; height: 1111px;
    background: var(--strip);
  }
  .brand-mark {
    position: absolute; left: 0; top: 150px; width: 244px;
    display: flex; align-items: center; justify-content: center; gap: 8px;
  }
  .brand-mark__dot {
    width: 10px; height: 10px; border-radius: 50%;
    background: var(--ink);
  }
  .brand-mark__name {
    font-family: "Cormorant SC", serif;
    font-weight: 500; font-size: 22px; letter-spacing: 0.02em;
    color: var(--ink);
  }
  .label {
    position: absolute;
    width: 29em; height: 38.9em;
    filter: drop-shadow(0 0.4em 0.8em rgba(0,0,0,0.25));
  }
  .label--flat { left: 98px; top: 637px; font-size: 10px; }
  .label--feature { left: 530px; top: 590px; font-size: 12px; }
  .label__shape { position: absolute; inset: 0; width: 100%; height: 100%; }
  .label__paper { fill: var(--paper); }
  .label__notch { fill: var(--gold); }
  .label__art {
    position: absolute; left: 14em; top: 8.2em;
    width: 11.2em; height: 20.4em;
    transform: translateX(-50%);
    margin-left: 1.4em;
    border-radius: 45% 45% 40% 40%;
    background: radial-gradient(ellipse at 45% 55%, var(--art-dark) 0%, #8a8580 45%, var(--art-leaf) 75%, rgba(233,169,42,0) 100%);
    opacity: 0.75;
  }
  .label__text {
    position: absolute; left: 0; right: 0; top: 31.2em;
    text-align: center;
  }
  .label__estate {
    font-family: "Cormorant SC", serif;
    font-weight: 500; font-size: 2.2em; line-height: 1;
  }
  .label__grape {
    font-family: "Pinyon Script", cursive;
    font-size: 3em; line-height: 1.05;
  }
  .label__appellation {
    font-family: "Cormorant Garamond", serif;
    font-size: 1.35em; letter-spacing: 0.45em;
    margin-left: 0.45em; line-height: 1.1;
  }
</style>
</head>
<body>
  <aside class="brand-strip">
    <div class="brand-mark">
      <span class="brand-mark__dot"></span>
      <span class="brand-mark__name">Clos des Aubrelles</span>
    </div>
  </aside>

  <article class="label label--flat">
    <svg class="label__shape" viewBox="0 0 290 389" preserveAspectRatio="none" aria-hidden="true">
      <path class="label__paper" d="M0,0 C60,0 118,18 145,68 C172,18 230,0 290,0 L290,389 L0,389 Z"/>
      <path class="label__notch" d="M45,9 C95,16 128,40 145,72 C162,40 195,16 245,9 C200,22 166,46 145,82 C124,46 90,22 45,9 Z"/>
    </svg>
    <div class="label__art" role="img" aria-label="Ink illustration of a woman with long flowing hair raising a grape, wreathed in golden vine leaves"></div>
    <div class="label__text">
      <p class="label__estate">Clos des Aubrelles</p>
      <p class="label__grape">Chenin</p>
      <p class="label__appellation">VOUVRAY</p>
    </div>
  </article>

  <article class="label label--feature">
    <svg class="label__shape" viewBox="0 0 290 389" preserveAspectRatio="none" aria-hidden="true">
      <path class="label__paper" d="M0,0 C60,0 118,18 145,68 C172,18 230,0 290,0 L290,389 L0,389 Z"/>
      <path class="label__notch" d="M45,9 C95,16 128,40 145,72 C162,40 195,16 245,9 C200,22 166,46 145,82 C124,46 90,22 45,9 Z"/>
    </svg>
    <div class="label__art" role="img" aria-label="Ink illustration of a woman with long flowing hair raising a grape, wreathed in golden vine leaves"></div>
    <div class="label__text">
      <p class="label__estate">Clos des Aubrelles</p>
      <p class="label__grape">Chenin</p>
      <p class="label__appellation">VOUVRAY</p>
    </div>
  </article>
</body>
</html>
```